Flyer-Design für traditionelles Dorffest
Zielgruppe
Benötigen Flyer/Plakat design A4 Doppelseite für traditionelles Dorffest.
Aufgabenstellung
Das Design soll einem traditionellen Dorffest der Schützenkompanie entsprechen. (Farben: Dunkelgrün oder Rot / Weiß)
Text Vorderseite:
- Die Schützenkompanie Obermoosbach lädt zum Obermoosbacher Dorffest. (Überschrift Obermoosbacher Dorffest groß)
- Samstag 10. August 2019
- Erstmals mit 'Riesen-Fußball-Dart' Turnier ab 14 Uhr
- 17 Uhr Einmarsch der Musikkapelle Obermoosbach mit anschließendem Konzert im Festzelt
- Stimmungsabend mit 'Die fesch'n Gamsler'
- zugestellt durch briefweg.at an einen Haushalt (Kleiner Hinweiß rechts oben)
- Eintritt: 5€ (Kleiner Schriftzug)
- Mit Schießbude, Wein- und Kaffeebar, Weißbierbar, Schützenbar und großer Tombola
Logos Vorderseite:
- Logo Musik 'Die fesch'n Gamsler'.
- Tiroler Adler (Schützen) Eventuell im Hintergrund oder Modifizieren
- Eventuell Bild von Hinterthiersee mit einbauchen (Hintergrund)
Text Hinterseite:
- Überschrift groß: 'Riesen-Fußball-Dart' Turnier
- Beginn um 14 Uhr
- 3 Spieler pro Team
- Startgebühr: 30 € pro Team (Damen, Herren oder Mixed Teams möglich) / Kinderteams 15 €
- Für Unfälle jeglicher Art wird vom Veranstalter keine Haftung übernommen! (Kleine Schrift)
- Wir achten auf den Jugendschutz! (Kleine Schrift)
- Überschrift groß: 'Heimfahrservice innerhalb von Bergtal'
Auf Euer Kommen freut sich die Schützenkompanie Obermoosbach!
Logos Rückseite Sponsoren: Kornkasse Bergtal, Laufwerker Obermoosbach, Jausenstation Brunnalm, Loidlmayr Bau, Metzgerei Stangl, Zitherbau Egger, varolin GmbH, Sanitär Technik Aubing
Logos im Anhang. Foto von Hinterthiersee und Tiroler Adler bei Bedarf via Mail (Da nicht mehr Anhänge möglich sind).
Bei Fragen freue Ich mich über Ihre Nachricht.
Vielen Dank für die Vorschläge.

```html
<!DOCTYPE html>
<html lang="de">
<head>
<meta charset="utf-8">
<title>Riesen-Fußball-Dart Turnier – Schützenkompanie Obermoosbach</title>
<link href="https://fonts.googleapis.com/css2?family=Rammetto+One&family=Barlow+Condensed:wght@500;600&display=swap" rel="stylesheet">
<style>
  :root {
    --photo-sky: #b9bcc0;
    --photo-ground: #8d8f8c;
    --panel: rgba(62, 92, 72, 0.9);
    --panel-dark: rgba(35, 55, 42, 0.55);
    --white: #ffffff;
    --ink: #2f4a3a;
  }
  * { margin: 0; padding: 0; box-sizing: border-box; }
  html, body { width: 848px; height: 1200px; overflow: hidden; }
  body {
    position: relative;
    background: linear-gradient(180deg, var(--photo-sky) 0%, #9ea39d 45%, var(--photo-ground) 100%);
    font-family: "Barlow Condensed", "Arial Narrow", sans-serif;
    color: var(--white);
  }
  .backdrop-photo { position: absolute; inset: 0; }
  .panel {
    position: absolute; left: 36px; top: 49px; width: 775px; height: 1102px;
    background: var(--panel);
  }
  .board-photo {
    position: absolute; left: 230px; top: 340px; width: 420px; height: 440px;
    border-radius: 50%;
    background: radial-gradient(circle, rgba(40,60,48,0.25) 0%, var(--panel-dark) 70%, rgba(0,0,0,0) 72%);
  }
  .frame { position: absolute; left: 0; top: 0; width: 848px; height: 1200px; }
  .rifles {
    position: absolute; left: 511px; top: 293px; width: 256px; height: 252px;
    background: rgba(255,255,255,0.14);
  }
  .headline {
    position: absolute; left: 88px;
    font-family: "Rammetto One", "Arial Black", sans-serif;
    font-weight: 400; white-space: nowrap; line-height: 1;
  }
  .title { top: 142px; font-size: 55px; line-height: 70px; }
  .subhead { font-size: 27px; }
  .big { font-size: 37px; line-height: 49px; top: 788px; }
  .text {
    position: absolute; left: 88px; font-weight: 600; white-space: nowrap; line-height: 1.2;
  }
  .t-lg { font-size: 26px; }
  .t-md { font-size: 23px; }
  .indent { padding-left: 16px; }
  .sponsors {
    position: absolute; left: 56px; top: 957px; width: 736px; height: 114px;
    background: var(--white); color: var(--ink);
    font-family: "Barlow Condensed", "Arial Narrow", sans-serif; font-weight: 600;
  }
  .sponsor-row {
    position: absolute; left: 0; width: 100%;
    display: flex; justify-content: space-around; align-items: center;
  }
  .row-top { top: 14px; height: 44px; }
  .row-bottom { top: 66px; height: 40px; padding: 0 110px; }
  .sponsor { display: flex; align-items: center; gap: 6px; font-size: 19px; white-space: nowrap; }
  .mark { width: 18px; height: 18px; background: var(--ink); }
</style>
</head>
<body>
  <div class="backdrop-photo" role="img" aria-label="Foto eines aufblasbaren Fußball-Dartboards im Freien vor Bäumen und Gebäuden"></div>

  <div class="panel"></div>
  <div class="board-photo" role="img" aria-label="Durchscheinendes Fußball-Dartboard im Hintergrund"></div>

  <svg class="frame" viewBox="0 0 848 1200" aria-hidden="true">
    <g fill="none" stroke="#ffffff" stroke-width="1.5">
      <rect x="50" y="65" width="748" height="1071"/>
      <rect x="56" y="71" width="736" height="1059"/>
    </g>
  </svg>

  <div class="rifles" role="img" aria-label="Zwei gekreuzte Gewehre als Strichzeichnung"></div>

  <h1 class="headline title">Riesen-Fußball-<br>Dart‘ Turnier</h1>

  <div class="headline subhead" style="top:310px">Beginn um 14 Uhr</div>
  <p class="text t-lg" style="top:346px">3 Spieler pro Team</p>

  <div class="headline subhead" style="top:423px">Startgebühr:</div>
  <p class="text t-lg" style="top:458px">- 30 € pro Team (Damen, Herren oder Mixed<br><span class="indent">Teams möglich)</span></p>
  <p class="text t-lg" style="top:532px">- Kinderteams 15 €</p>

  <p class="text t-md" style="top:614px">Für Unfälle jeglicher Art wird vom Veranstalter keine Haftung übernommen!</p>

  <div class="headline subhead" style="top:658px">Anmeldungen an:</div>
  <p class="text t-md" style="top:691px">Email: info@gasthof-almrausch.at</p>
  <p class="text t-md" style="top:723px">Tel.: +43 680 55 13 472</p>

  <h2 class="headline big">Heimfahrservice<br>innerhalb von Bergtal</h2>

  <p class="text t-lg" style="top:915px">Auf Euer Kommen freut sich die Schützenkompanie Obermoosbach!</p>

  <div class="sponsors">
    <div class="sponsor-row row-top">
      <span class="sponsor">Kornkasse Bergtal <span class="mark"></span></span>
      <span class="sponsor">Laufwerker Obermoosbach</span>
      <span class="sponsor">Jausenstation Brunnalm</span>
      <span class="sponsor">Loidlmayr Bau</span>
    </div>
    <div class="sponsor-row row-bottom">
      <span class="sponsor">Metzgerei Stangl</span>
      <span class="sponsor">Zitherbau Egger</span>
      <span class="sponsor">varolin GmbH</span>
      <span class="sponsor">Sanitär Technik Aubing</span>
    </div>
  </div>
</body>
</html>
```